Looking for a Lumora Book Cover

My book has been online for a while and I am now looking for a professional cover for it as it has been very well received.

You can view the book here and all the details about it:

https://www.pagevaultshop.example/dp/X7Q2KRMTPL#readerNotes

Not sure what I am looking for as a design, just open to your ideas.

I want something different that will stand out please.

Thanks
Owen

```html
<!DOCTYPE html>
<html lang="en">
<head>
<meta charset="utf-8">
<title>Roots and Resilience – Book Cover</title>
<link rel="stylesheet" href="https://fonts.googleapis.com/css2?family=Bebas+Neue&family=Poppins:wght@300;400;700;800&display=swap">
<style>
  :root {
    --page-bg: #ffffff;
    --cover-black: #000000;
    --title-orange: #c87314;
    --white: #ffffff;
    --band-red: #c41e2a;
    --band-dark: #1a0306;
    --photo-light: #6a6a6a;
    --photo-mid: #2c2c2c;
  }
  * { margin: 0; padding: 0; box-sizing: border-box; }
  html, body {
    width: 1200px; height: 1200px; overflow: hidden;
    background: var(--page-bg);
  }
  .cover {
    position: absolute;
    left: 216px; top: 48px;
    width: 767px; height: 1103px;
    background: var(--cover-black);
    overflow: hidden;
  }
  .cover h1 { font-weight: 400; }
  .title-main {
    position: absolute; left: 0; width: 100%;
    text-align: center;
    font-family: "Bebas Neue", "Oswald", sans-serif;
    font-weight: 400;
    color: var(--title-orange);
    line-height: 1;
    white-space: nowrap;
  }
  .title-roots { top: 10px; font-size: 300px; letter-spacing: 1px; }
  .title-resilience { top: 318px; font-size: 170px; letter-spacing: 2px; }
  .title-and {
    position: absolute; top: 266px; left: 0; width: 100%;
    text-align: center;
    font-family: "Bebas Neue", "Oswald", sans-serif;
    font-weight: 400;
    font-size: 61px; line-height: 1; color: var(--white);
  }
  .rule {
    position: absolute; top: 293px; height: 3px; width: 234px;
    background: var(--white);
  }
  .rule-left { left: 91px; }
  .rule-right { left: 430px; }
  .tagline-band {
    position: absolute; top: 511px; left: 0; width: 100%; height: 80px;
    background: radial-gradient(ellipse 55% 120% at 55% 50%, var(--band-red) 0%, #7a0f17 55%, var(--band-dark) 100%);
    display: flex; align-items: center; justify-content: center;
  }
  .tagline {
    font-family: "Bebas Neue", "Oswald", sans-serif;
    font-size: 35px; line-height: 1; color: var(--white);
    white-space: nowrap;
  }
  .cover-photo {
    position: absolute; top: 591px; right: 0; width: 488px; height: 512px;
    background:
      radial-gradient(ellipse 45% 50% at 60% 45%, var(--photo-light) 0%, var(--photo-mid) 55%, transparent 100%),
      linear-gradient(90deg, var(--cover-black) 0%, #1a1a1a 45%, #252525 100%);
  }
  .subtitle {
    position: absolute; top: 655px; left: 71px;
    font-family: "Poppins", sans-serif;
    font-size: 26px; line-height: 37px;
    color: var(--white); font-weight: 300;
    white-space: nowrap;
  }
  .subtitle .accent { color: var(--title-orange); }
  .subtitle .strong { color: var(--title-orange); font-weight: 700; }
  .subtitle .big { color: var(--title-orange); font-weight: 700; font-size: 39px; }
  .author-bar {
    position: absolute; left: 0; bottom: 0; width: 100%; height: 80px;
    background: linear-gradient(90deg, rgba(0,0,0,0.9) 0%, rgba(30,28,26,0.8) 60%, rgba(50,46,42,0.7) 100%);
    display: flex; align-items: center; justify-content: center;
  }
  .author-name {
    font-family: "Poppins", sans-serif;
    font-size: 30px; font-weight: 400; color: var(--white);
  }
</style>
</head>
<body>
  <main class="cover">
    <h1>
      <span class="title-main title-roots">ROOTS</span>
      <span class="rule rule-left"></span>
      <span class="title-and">AND</span>
      <span class="rule rule-right"></span>
      <span class="title-main title-resilience">RESILIENCE</span>
    </h1>
    <div class="tagline-band">
      <p class="tagline">A Celebration of Culture, Struggle and Achievement</p>
    </div>
    <div class="cover-photo" role="img" aria-label="Black and white portrait of a thoughtful young woman resting her chin on her fist"></div>
    <p class="subtitle">
      <span class="strong">The History</span>,<br>
      <span class="accent">Resistance</span> and <span class="accent">Excellence</span><br>
      of Blac <span class="strong">People in Africa and</span><br>
      <span class="strong">the</span> <span class="big">Diaspora</span>
    </p>
    <div class="author-bar">
      <p class="author-name">Desmond Hale</p>
    </div>
  </main>
</body>
</html>
```